依頼詳細
春に向け新しくリニューアルオープンするお店です。
チラシを沢山の人に見て頂き、お店に来ていただいたり、ネットでの販売やピクセルノートも見て頂いたりと、手にとって頂けるようなチラシを作って頂きたいです。
記載項目
『***』 白砂糖を使わず、自然派甘味料とオーガニック素材を厳選、低糖質で最高の満足感を得るSweetsが完成。
体に優しく、健康や糖分が気になる方にも安心してお召し上がり頂けます。

完全予約制
100%手作り
健康志向
糖質制限
こだわり抜いた最高傑作を

住所 岐阜県北方市桜台字東原4815−27
ご予約は、***までお電話ください

***
サイズ
A4
ページ数
片面
希望イメージ
シンプル 複雑
単色 カラフル
暗い 明るい
日常 高級
遊び心 厳粛
未来的 伝統的
女性的 男性的
希望する色
水色系、茶系、無彩色系
補足説明
記載項目に書いた内容だけではなくイメージに合えば文言も付け加えて頂いても構いません
添付のロゴと
チラシは以前に使っていたものになります。
写真は使用はお任せしたいです。

```html
<!DOCTYPE html>
<html lang="ja">
<head>
<meta charset="utf-8">
<title>Belle Douceur Healthy Sweets</title>
<link rel="stylesheet" href="https://fonts.googleapis.com/css2?family=Shippori+Mincho:wght@400;600&family=Cormorant+Garamond:wght@400;500&display=swap">
<style>
  :root {
    --paper: #ffffff;
    --ink: #2b2623;
    --night: #1c1b1a;
    --cocoa: #3b2a22;
    --gold: #b8995a;
    --berry: #a8322c;
    --mousse: #8a5a44;
    --slate: #2c2b2a;
  }
  * { margin: 0; padding: 0; box-sizing: border-box; }
  html, body { width: 849px; height: 1200px; overflow: hidden; background: var(--paper); }
  .flyer {
    position: relative; width: 849px; height: 1200px; overflow: hidden;
    background: var(--paper); color: var(--ink);
    font-family: "Shippori Mincho", serif;
  }
  .headline-band {
    position: absolute; left: 606px; top: 0; width: 243px; height: 440px;
    background: var(--night);
  }
  .photo-cake {
    position: absolute; left: 205px; top: 18px; width: 401px; height: 420px;
    background:
      radial-gradient(ellipse 38% 10% at 42% 16%, rgba(168,50,44,0.85) 0%, rgba(168,50,44,0) 100%),
      radial-gradient(ellipse 48% 26% at 45% 40%, #9b6a52 0%, rgba(122,80,60,0.9) 55%, rgba(60,40,32,0) 100%),
      radial-gradient(ellipse 60% 14% at 50% 78%, #3a3836 0%, rgba(58,56,54,0) 100%),
      linear-gradient(180deg, #494846 0%, #2f2e2d 60%, #222120 100%);
  }
  .photo-plate {
    position: absolute; left: 212px; top: 438px; width: 637px; height: 492px;
    background:
      radial-gradient(ellipse 30% 26% at 36% 48%, #5a3426 0%, rgba(70,40,30,0.6) 55%, rgba(40,38,36,0) 100%),
      radial-gradient(ellipse 50% 46% at 42% 52%, #3d3c3a 0%, #2b2a29 70%, rgba(30,29,28,0) 100%),
      radial-gradient(circle 10px at 62% 40%, var(--berry) 0%, rgba(168,50,44,0) 100%),
      radial-gradient(circle 10px at 22% 20%, var(--berry) 0%, rgba(168,50,44,0) 100%),
      linear-gradient(180deg, #1e1d1c 0%, #171615 100%);
  }
  .headline {
    position: absolute; right: 24px; top: 28px; z-index: 2;
    writing-mode: vertical-rl; color: #fff;
    font-size: 76px; font-weight: 600; line-height: 1.25; letter-spacing: 0.06em;
  }
  .intro {
    position: absolute; left: 40px; top: 88px; height: 900px; z-index: 2;
    writing-mode: vertical-rl; font-size: 20px; line-height: 2; letter-spacing: 0.26em;
  }
  .features {
    position: absolute; left: 262px; top: 842px; display: flex; gap: 26px; list-style: none; z-index: 2;
  }
  .features li {
    width: 82px; height: 82px; border: 1.5px solid var(--gold); border-radius: 50%;
    background: rgba(255,255,255,0.94); color: var(--gold);
    display: flex; align-items: center; justify-content: center; text-align: center;
    font-size: 15px; line-height: 1.3;
  }
  .brand {
    position: absolute; left: 0; top: 955px; width: 849px;
    display: flex; align-items: center; justify-content: center; gap: 18px; color: var(--gold);
  }
  .brand-mark { width: 66px; height: 66px; border: 1.5px solid var(--gold); border-radius: 50%; }
  .brand-name { font-family: "Cormorant Garamond", serif; font-size: 58px; font-weight: 500; line-height: 1; }
  .brand-tag { font-family: "Cormorant Garamond", serif; font-size: 17px; letter-spacing: 0.35em; text-align: center; margin-top: 6px; }
  .contact { position: absolute; left: 40px; top: 1090px; width: 690px; }
  .address { font-size: 13px; margin-bottom: 8px; }
  .reserve { display: flex; align-items: center; gap: 8px; font-size: 23px; white-space: nowrap; }
  .reserve svg { width: 24px; height: 24px; flex: none; }
  .url { font-family: "Cormorant Garamond", serif; font-size: 18px; margin-top: 8px; }
  .reserve-only {
    position: absolute; right: 38px; top: 1118px; width: 62px; height: 62px;
    background: var(--cocoa); color: #fff; font-size: 15px; line-height: 1.3;
    display: flex; align-items: center; justify-content: center; text-align: center;
  }
</style>
</head>
<body>
<main class="flyer">
  <div class="headline-band"></div>
  <div class="photo-cake" role="img" aria-label="ストロベリーを飾ったチョコレートムースケーキの写真"></div>
  <div class="photo-plate" role="img" aria-label="黒い皿に盛られたチョコレートケーキとフォークの写真"></div>

  <h1 class="headline">こだわり抜いた<br>最高傑作を</h1>

  <p class="intro">白砂糖を使わず、自然派甘味料とオーガニック素材を厳選、<br>低糖質で最高の満足感を得るSweetsが完成。<br>体に優しく、健康や糖分が気になる方にも安心してお召し上がり頂けます。</p>

  <ul class="features">
    <li>100%<br>手作り</li>
    <li>健康<br>志向</li>
    <li>糖質<br>制限</li>
  </ul>

  <div class="brand">
    <span class="brand-mark"></span>
    <div>
      <div class="brand-name">Belle Douceur</div>
      <div class="brand-tag">HEALTHY SWEETS</div>
    </div>
  </div>

  <div class="contact">
    <p class="address">岐阜県北方市桜台字東原4815−27</p>
    <p class="reserve">
      <svg viewBox="0 0 24 24" aria-hidden="true"><path fill="#2b2623" d="M6.6 10.8a15.2 15.2 0 0 0 6.6 6.6l2.2-2.2a1 1 0 0 1 1-.25 11.4 11.4 0 0 0 3.6.57 1 1 0 0 1 1 1V20a1 1 0 0 1-1 1A17 17 0 0 1 3 4a1 1 0 0 1 1-1h3.5a1 1 0 0 1 1 1c0 1.25.2 2.45.57 3.57a1 1 0 0 1-.25 1z"/></svg>
      ご予約は、「090-5821-7364」高橋までお電話ください。
    </p>
    <p class="url">https://belledouceur.example.shop</p>
  </div>
  <div class="reserve-only">完全<br>予約制</div>
</main>
</body>
</html>
```